Gentle Cradle Pregnancy and Baby Massage

I need a web design for a new business, GENTLE CRADLE PREGNANCY AND BABY MASSAGE that I am in the process of setting up in the suburbs of Perth, Western Australia. The business is owned and operated by myself and my intention is to service Pregnant Mothers and Parents of Young Babies that would benefit from massage. I would like to have a "Home Page" and pages for "About Me", "Pregnancy Massage", "Baby Massage", a Pricing Page for Pregnancy Massage Sessions, a Pricing Page for Baby Massage Sessions, and a "Contact Me" page to allow clients to either contact me with queries or book available pregnancy massage sessions on a particular day of the week. I would also like a "News" page that would include articles I have written, news about new courses and a link to my Chatterlink page (yet to be set up). I would like to keep the colour schemes similar to my logo design colours. I need the design to be easy to follow and to appeal to a younger audience (20's to mid 30's).
The target audience is pregnant mothers-to-be wishing to receive massage treatments, and new parents and grandparents of small babies that would like to learn how to massage their babies.
The look and feel should be modern, professional, elegant and feminine.
I need the design to be in a standard format such that I can update the content by myself ( and does not need specialised software) as the company and business progresses.

Target Market(s)

Contact Information for Business Card

Card should have rounded edges. Design should have the same "feel" as the website. Contact Details of my business address, mobile phone, email and website should be included.

Requirements
Must have
• Same colours as logo design. In cmyk system, the colours are: 20,60,0,0 which best result is pantone 681 and 40,40,0,0 which best result is pantone 2645. Card should include the logo design.

```html
<!DOCTYPE html>
<html lang="en">
<head>
<meta charset="utf-8">
<title>Gentle Cradle Pregnancy and Baby Massage</title>
<link rel="stylesheet" href="https://fonts.googleapis.com/css2?family=Raleway:ital,wght@0,400;0,500;0,600;0,700;1,400&family=Yellowtail&display=swap">
<style>
:root{
  --purple:#8c80bb;
  --purple-dark:#7a6eab;
  --pink:#bb6aa2;
  --pink-dark:#a85790;
  --ink:#333333;
  --muted:#666666;
  --field:#efefef;
  --white:#ffffff;
  --blush:#f3e6ec;
}
*{margin:0;padding:0;box-sizing:border-box}
html,body{width:1200px;height:3364px;overflow:hidden}
body{position:relative;background:var(--white);font-family:"Raleway",sans-serif;color:var(--ink)}
.abs{position:absolute}
.script{font-family:"Yellowtail",cursive;font-weight:400}
.btn{position:absolute;display:flex;align-items:center;justify-content:center;background:var(--pink);color:var(--white);font-family:"Raleway",sans-serif;font-weight:500;text-transform:uppercase;box-shadow:0 3px 6px rgba(0,0,0,.25)}

/* header */
.site-header{position:absolute;left:0;top:0;width:1200px;height:137px;background:var(--white)}
.brand{position:absolute;left:70px;top:22px;display:flex;align-items:center;gap:12px}
.brand-dot{width:44px;height:44px;border-radius:50%;background:var(--pink)}
.brand-name{font-weight:600;color:var(--pink);font-size:19px;line-height:23px}
.call{position:absolute;left:734px;top:18px;display:flex;gap:12px;align-items:center}
.call-label{font-size:13px;font-style:italic;color:var(--pink);line-height:16px}
.call-number{font-size:24px;font-weight:500;color:var(--pink);line-height:26px}
.header-book{left:947px;top:15px;width:177px;height:56px;font-size:22px}
.main-nav{position:absolute;right:76px;top:96px;display:flex;gap:30px;font-size:15px;font-weight:500;text-transform:uppercase}
.main-nav a{color:var(--ink);text-decoration:none;padding-bottom:14px}
.main-nav a.active{color:var(--purple);border-bottom:3px solid var(--purple)}

/* hero */
.hero{position:absolute;left:0;top:137px;width:1200px;height:543px;background:linear-gradient(180deg,#cfc4bf 0%,#e8ddd6 35%,#bfb0a8 70%,#d9ccc3 100%)}
.hero-title{position:absolute;left:0;width:1200px;top:168px;text-align:center;color:var(--white);font-size:50px;font-weight:600;text-shadow:0 2px 6px rgba(0,0,0,.35)}
.hero-sub{position:absolute;left:0;width:1200px;top:236px;text-align:center;color:#2a2a2a;font-size:46px}
.hero-btn{left:375px;top:323px;width:450px;height:58px;font-size:21px}
.hero-arrow{position:absolute;top:238px}

/* welcome band */
.welcome{position:absolute;left:0;top:680px;width:1200px;height:269px;background:var(--purple);color:var(--white);text-align:center}
.welcome h2{position:absolute;top:40px;width:100%;font-size:46px}
.welcome .tag{position:absolute;top:104px;width:100%;font-size:18px}
.welcome p{position:absolute;left:175px;width:850px;top:144px;font-size:13.5px;line-height:26px;color:#efeaf7}
.learn-btn{left:510px;top:920px;width:188px;height:58px;font-size:20px}

/* about */
.about-photo{position:absolute;left:94px;top:1025px;width:393px;height:395px;background:var(--purple);border:4px solid var(--purple)}
.about-photo .photo{position:absolute;left:0;top:0;width:385px;height:320px;background:linear-gradient(150deg,#d8b7a4,#e9cbb8 45%,#c98a73)}
.about-photo .label{position:absolute;top:325px;width:100%;text-align:center;color:var(--white);font-size:44px}
.cert{position:absolute;left:572px;top:1054px;display:flex;gap:30px;align-items:center}
.cert-badge{width:90px;height:90px;border-radius:50%;background:#e7dff3}
.about-text{position:absolute;left:572px;top:1196px;width:470px;font-size:16px;font-style:italic;line-height:28px;color:var(--ink)}
.arrows{position:absolute;left:568px;top:1300px;display:flex;gap:16px}
.round-arrow{width:56px;height:56px;border-radius:50%;background:var(--pink);display:flex;align-items:center;justify-content:center}

/* services */
.services{position:absolute;left:0;top:1487px;width:1200px;height:521px;background:linear-gradient(180deg,#f6f3f3,#ece4e4 60%,#f4efef)}
.services h2{position:absolute;top:54px;width:100%;text-align:center;color:var(--purple);font-size:46px}
.services .tag{position:absolute;top:122px;width:100%;text-align:center;color:var(--pink);font-size:17px}
.service{position:absolute;top:174px;width:280px;height:280px;border-radius:50%;border:5px solid #4a4a4a;box-shadow:0 6px 12px rgba(0,0,0,.3);overflow:hidden}
.service .photo{position:absolute;inset:0}
.service .ribbon{position:absolute;left:40px;top:166px;width:240px;height:56px;background:var(--pink);clip-path:polygon(14% 0,100% 0,100% 100%,0 100%);color:var(--white);font-size:19px;font-weight:600;font-style:italic;display:flex;align-items:center;justify-content:center}

/* testimonials */
.testimonials{position:absolute;left:0;top:2008px;width:1200px;height:280px;background:var(--pink);color:var(--white)}
.testimonials h2{position:absolute;top:38px;width:100%;text-align:center;font-size:44px}
.quote-avatar{position:absolute;left:136px;top:90px;width:130px;height:130px;border-radius:50%;border:4px solid var(--white);background:linear-gradient(160deg,#c9a28a,#e6cdbd);box-shadow:0 4px 8px rgba(0,0,0,.3)}
.quote-mark{position:absolute;left:76px;top:88px;width:132px;height:132px;border-radius:50%;border:3px solid var(--white);display:flex;align-items:center;padding-left:14px;font-size:54px;font-weight:700;line-height:1}
.quote-text{position:absolute;left:287px;top:100px;width:800px;font-size:14px;line-height:27px}
.quote-name{position:absolute;left:292px;top:205px;font-size:22px}
.dots{position:absolute;left:1154px;top:92px;display:flex;flex-direction:column;gap:15px}
.dots span{width:15px;height:15px;border-radius:50%;background:var(--white);opacity:.9}

/* booking */
.booking{position:absolute;left:83px;top:2369px;width:1034px;height:311px;border:3px solid var(--purple)}
.booking h2{position:absolute;left:50%;transform:translateX(-50%);top:-34px;padding:0 22px;background:var(--white);color:var(--purple);font-size:44px;white-space:nowrap}
.booking .tag{position:absolute;top:46px;width:100%;text-align:center;font-size:17px;font-style:italic;color:var(--muted)}
.field{position:absolute;background:var(--field);font-size:13px;color:#8a8a8a;padding:14px 14px}
.submit-btn{left:516px;top:2651px;width:168px;height:59px;font-size:20px;font-weight:600}

/* contact strip */
.contact-strip{position:absolute;left:0;top:2770px;width:1200px;height:247px;background:linear-gradient(90deg,#f5f0f1,#f8f1f3 50%,#f6dde2)}
.contact-item{position:absolute;top:48px;width:300px;text-align:center}
.contact-icon{width:100px;height:100px;margin:0 auto;border-radius:50%;background:var(--pink);display:flex;align-items:center;justify-content:center}
.contact-item p{margin-top:30px;font-size:18px;font-weight:500;color:var(--ink);line-height:24px}

/* footer */
.site-footer{position:absolute;left:0;top:3017px;width:1200px;height:347px;background:var(--purple);color:var(--white);text-align:center}
.footer-brand{position:absolute;top:48px;width:100%;display:flex;justify-content:center;align-items:center;gap:14px}
.footer-brand .brand-dot{background:var(--white)}
.footer-brand .brand-name{color:var(--white);font-size:22px;line-height:27px;text-align:left}
.social{position:absolute;left:578px;top:180px;width:44px;height:44px;border-radius:50%;background:var(--pink)}
.footer-nav{position:absolute;top:250px;width:100%;font-size:14px}
.footer-nav a{color:var(--white);text-decoration:none;padding:0 10px}
.footer-nav .sep{opacity:.8}
.copyright{position:absolute;top:284px;width:100%;font-size:14px}
.copyright b{font-weight:700}
</style>
</head>
<body>

<header class="site-header">
  <div class="brand">
    <span class="brand-dot"></span>
    <span class="brand-name">Gentle Cradle<br>Pregnancy and Baby Massage</span>
  </div>
  <div class="call">
    <svg width="44" height="44" viewBox="0 0 24 24" aria-hidden="true"><path fill="#bb6aa2" d="M6.6 10.8a15.1 15.1 0 0 0 6.6 6.6l2.2-2.2c.3-.3.7-.4 1-.2 1.1.4 2.3.6 3.6.6.6 0 1 .4 1 1V20c0 .6-.4 1-1 1A17 17 0 0 1 3 4c0-.6.4-1 1-1h3.5c.6 0 1 .4 1 1 0 1.3.2 2.5.6 3.6.1.3 0 .7-.2 1z"/></svg>
    <div>
      <div class="call-label">Call Us Today :-</div>
      <div class="call-number">041 0555 193</div>
    </div>
  </div>
  <div class="btn header-book">Book Now</div>
  <nav class="main-nav">
    <a class="active">Home</a><a>About Me</a><a>Pregnancy Massage</a><a>Baby Massage</a><a>Price</a><a>News</a><a>Contact Us</a>
  </nav>
</header>

<section class="hero" role="img" aria-label="Photo of a therapist's hands held above a pregnant woman's belly during a massage">
  <svg class="hero-arrow" style="left:26px" width="24" height="56" viewBox="0 0 24 56" aria-hidden="true"><path d="M20 4 4 28l16 24" fill="none" stroke="#fff" stroke-width="2"/></svg>
  <svg class="hero-arrow" style="right:26px" width="24" height="56" viewBox="0 0 24 56" aria-hidden="true"><path d="M4 4l16 24L4 52" fill="none" stroke="#fff" stroke-width="2"/></svg>
  <h1 class="hero-title">It's All About You</h1>
  <div class="hero-sub script">Gentle Cradle pregnancy And Baby Massage</div>
  <div class="btn hero-btn">Book Pregnancy Massage Sessions</div>
</section>

<section class="welcome">
  <h2 class="script">Welcome To Gentle Cradle</h2>
  <div class="tag">Pregnancy And Baby Massage</div>
  <p>Maren is a Practitioner of Pregnancy Massage, and a Paediatric Massage Consultant. She completed her training with Bloom Prenatal Academy, and the Little Touch Learning Network. The LTLN is endorsed by the Southern Guild of Birth Carers, The Coastal Wellness Practice Council, and accredited by the Federation of Bodywork Practitioners</p>
</section>
<div class="btn learn-btn">Learn More</div>

<section class="about">
  <div class="about-photo">
    <div class="photo" role="img" aria-label="Photo of two sleeping newborn babies wrapped in a soft blanket"></div>
    <div class="label script">Gentle Cradle</div>
  </div>
  <div class="cert">
    <span class="cert-badge" role="img" aria-label="Certification badge"></span>
  </div>
  <p class="about-text">Gentle Cradle Pregnancy and Baby Massage was launched in 2017, offering massage for pregnant women, and instruction of baby massage to parents, grandparents and carers.</p>
  <div class="arrows">
    <span class="round-arrow"><svg width="20" height="20" viewBox="0 0 20 20" aria-hidden="true"><path d="M7 3l7 7-7 7" fill="none" stroke="#fff" stroke-width="2.5"/></svg></span>
    <span class="round-arrow"><svg width="20" height="20" viewBox="0 0 20 20" aria-hidden="true"><path d="M13 3l-7 7 7 7" fill="none" stroke="#fff" stroke-width="2.5"/></svg></span>
  </div>
</section>

<section class="services">
  <h2 class="script">Welcome To Gentle Cradle</h2>
  <div class="tag">Pregnancy And Baby Massage</div>
  <div class="service" style="left:104px">
    <div class="photo" role="img" aria-label="Photo of a pregnant woman relaxing during a massage" style="background:linear-gradient(150deg,#e9ddd4,#cdb6a6)"></div>
    <div class="ribbon">Pregnancy Massage</div>
  </div>
  <div class="service" style="left:461px">
    <div class="photo" role="img" aria-label="Photo of hands gently massaging a baby's feet" style="background:linear-gradient(150deg,#f0d8cb,#d9a993)"></div>
    <div class="ribbon">Baby Massage</div>
  </div>
  <div class="service" style="left:816px">
    <div class="photo" role="img" aria-label="Photo of a mother holding her baby" style="background:linear-gradient(150deg,#f2ece6,#b89a86)"></div>
    <div class="ribbon">Our Price</div>
  </div>
</section>

<section class="testimonials">
  <h2 class="script">Testimonials</h2>
  <div class="quote-mark">&ldquo;</div>
  <div class="quote-avatar" role="img" aria-label="Portrait photo of the client"></div>
  <p class="quote-text">" Lorem Ipsum is simply dummy text of the printing and typesetting industry. Lorem Ipsum has been the industry's standard dummy text ever since the 1500s, when an unknown printer took a galley of type " Lorem Ipsum is simply dummy text of the printing and typesetting industry. Lorem Ipsum has "</p>
  <div class="quote-name script">&mdash; Tessa Holloway</div>
  <div class="dots"><span></span><span></span><span></span><span></span></div>
</section>

<section class="booking">
  <h2 class="script">Book An Appointment</h2>
  <div class="tag">Need a free quote, or have a question? Get in touch!</div>
  <div class="field" style="left:33px;top:80px;width:312px;height:53px">Name*</div>
  <div class="field" style="left:358px;top:80px;width:312px;height:53px">Email*</div>
  <div class="field" style="left:683px;top:80px;width:310px;height:53px">Phone*</div>
  <div class="field" style="left:33px;top:145px;width:960px;height:112px">Message*</div>
</section>
<div class="btn submit-btn">Submit</div>

<section class="contact-strip">
  <div class="contact-item" style="left:94px">
    <div class="contact-icon"><svg width="40" height="40" viewBox="0 0 24 24" aria-hidden="true"><path fill="#fff" d="M12 2a7 7 0 0 0-7 7c0 5 7 13 7 13s7-8 7-13a7 7 0 0 0-7-7zm0 9.5A2.5 2.5 0 1 1 12 6.5a2.5 2.5 0 0 1 0 5z"/></svg></div>
    <p>Maren Ellison</p>
  </div>
  <div class="contact-item" style="left:451px">
    <div class="contact-icon"><svg width="38" height="38" viewBox="0 0 24 24" aria-hidden="true"><path fill="#fff" d="M6.6 10.8a15.1 15.1 0 0 0 6.6 6.6l2.2-2.2c.3-.3.7-.4 1-.2 1.1.4 2.3.6 3.6.6.6 0 1 .4 1 1V20c0 .6-.4 1-1 1A17 17 0 0 1 3 4c0-.6.4-1 1-1h3.5c.6 0 1 .4 1 1 0 1.3.2 2.5.6 3.6.1.3 0 .7-.2 1z"/></svg></div>
    <p>041 0555 193</p>
  </div>
  <div class="contact-item" style="left:835px">
    <div class="contact-icon"><svg width="40" height="40" viewBox="0 0 24 24" aria-hidden="true"><path fill="#fff" d="M3 5h18v14H3zm2 2v.5l7 5 7-5V7l-7 5z"/></svg></div>
    <p>maren.ellison@gentle-cradle.com.au</p>
  </div>
</section>

<footer class="site-footer">
  <div class="footer-brand">
    <span class="brand-dot"></span>
    <span class="brand-name">Gentle Cradle<br>Pregnancy and Baby Massage</span>
  </div>
  <span class="social" role="img" aria-label="Chatterlink"></span>
  <nav class="footer-nav">
    <a>Home</a><span class="sep">|</span><a>About me</a><span class="sep">|</span><a>Pregnancy Massage</a><span class="sep">|</span><a>Baby Massage</a><span class="sep">|</span><a>Price</a><span class="sep">|</span><a>News</a><span class="sep">|</span><a>Contact</a>
  </nav>
  <div class="copyright">&copy;<b>Gentle Cradle Pregnancy and Infant Massage</b>- 2017 All Right Reserved</div>
</footer>

</body>
</html>
```